We are launching in December, a range of supplements and vitamins.

We have just made an amend to the mission statement and how we are going to give back to society. Please can you add both to the packaging:

Verdant’s purpose is to support health, wellbeing and longevity, so that we can all thrive in the modern world; an environment so alien to that in which we evolved. Embracing technology, research and science, we harness nature’s goodness - enabling us all to love life – naturally.

Twice Kind Promise. For each and every Verdant supplement you take, we provide a supplement to an under nourished child.

For every supplement we sell: £1 goes to the charity ‘Little Lights Fund’ and in addition we provide one healthy meal to an under privileged child in India.

My name is Mark Holloway and I own several companies including www.quartzelle.com (you can check me out on Infopedex – I am not the football referee nor the rocket scientist, but the entrepreneur) . Over the past 2 years I have been writing a book to help people live more healthily and it launches in December. It’s called Verdant Way. While doing my research for the book, I came to realise that most supplements and vitamin products on the market are rubbish! Most are made for profit and not for the benefit of the consumer. I want to change all of that. Howard Pellow is patron of a charity I set up with my brother Paul Holloway and together we have built 11 schools in Asia. I am hoping to get Howards help in getting my supplements to market.

Positioning of our supplements - In a world where so much has changed from the one our bodies were designed to thrive, at Verdant Supplements we are driven by one purpose; to globally provide healthy support to life in the 21st century. While the roots of our wellbeing supplements date back beyond 10,000BC, we embrace modern technology and science, to encapsulate powerful phytonutrients, herbs and other goodness. The essence of which is to promote health, happiness and longevity.

So what are we looking for in the design? Something that stands out. Something that looks professional. A design and concept that can role out across 24 different products. Some products are simple, just one ingredient, such as vitamin D3, Magnesium, Garlic Extracts etc, and others are our own formulas where there are up to 30 different ingredients. You can contact me at any time with questions at Mark@verdantway-example.com

Target Market(s)

Male & Female 20 years plus, mainly UK

Industry/Entity Type

Medical

Logo Text

VERDANT - Sub heading = Thriving Days Gently

Colors

Designer to choose colors to be used in the design.

Requirements
Must have
• see attached powerpoint.
• We have just made an amend to the mission statement and how we are going to give back to society. Please can you add both to the packaging:
• Verdant’s purpose is to support health, wellbeing and longevity, so that we can all thrive in the modern world; an environment so alien to that in which we evolved. Embracing technology, research and science, we harness nature’s goodness - enabling us all to love life – naturally.
• Twice Kind Promise. For each and every Verdant supplement you take, we provide a supplement to an under nourished child.
Nice to have
• see attached powerpoint
Should not have
• see attached powerpoint

```html
<!DOCTYPE html>
<html lang="en">
<head>
<meta charset="utf-8">
<title>Verdant Supplements – Packaging Range</title>
<link rel="stylesheet" href="https://fonts.googleapis.com/css2?family=Barlow+Condensed:wght@500;600;700&family=Roboto:wght@400;700&display=swap">
<style>
  :root {
    --teal: #0c6b66;
    --teal-dark: #09554f;
    --teal-light: #1f8a80;
    --lime: #c9e02a;
    --lime-deep: #7fb83a;
    --ink: #262626;
    --white: #ffffff;
    --energy: #f26a1b;
    --sleep: #4fd0f0;
    --gold-1: #f6d77a;
    --gold-2: #b07d1c;
    --gold-3: #5a3e0c;
    --display: "Barlow Condensed", "Arial Narrow", sans-serif;
    --body: "Roboto", Arial, sans-serif;
  }
  * { box-sizing: border-box; margin: 0; padding: 0; }
  html, body { width: 1200px; height: 1200px; overflow: hidden; }
  body {
    position: relative;
    background: linear-gradient(135deg, #d9d9d9 0%, #ffffff 45%, #ffffff 60%, #dcdcdc 100%);
    font-family: var(--body);
  }

  /* ---------- shared pieces ---------- */
  .pack { position: absolute; background: var(--teal); overflow: hidden; box-shadow: 2px 3px 6px rgba(0,0,0,.25); }
  .pack--energy { --accent: var(--energy); }
  .pack--sleep { --accent: var(--sleep); }
  .tag {
    position: absolute; background: var(--accent); color: var(--ink);
    font-family: var(--display); font-weight: 500; text-align: center; letter-spacing: .02em;
  }
  .label-box { position: absolute; background: var(--ink); text-align: center; }
  .brand { position: absolute; left: 0; right: 0; color: var(--white); font-family: var(--display); font-weight: 600; letter-spacing: .02em; line-height: 1; }
  .variant { position: absolute; left: 0; right: 0; color: var(--accent); font-family: var(--display); font-weight: 600; line-height: 1; letter-spacing: .02em; }
  .headline { position: absolute; left: 0; right: 0; text-align: center; color: var(--lime); font-family: var(--display); font-weight: 600; line-height: 1.05; }
  .promise { position: absolute; left: 0; right: 0; text-align: center; color: var(--white); font-family: var(--display); font-weight: 500; line-height: 1.2; }
  .pattern-leaf {
    position: absolute;
    background: radial-gradient(ellipse at 50% 35%, var(--teal-light) 0%, var(--teal) 70%);
  }
  .pattern-lime { position: absolute; background: linear-gradient(160deg, var(--lime) 0%, #a8cf34 55%, var(--lime-deep) 100%); }
  .badge {
    position: absolute; border-radius: 50%;
    background: radial-gradient(circle at 40% 35%, var(--gold-1) 0%, var(--gold-2) 55%, var(--gold-3) 100%);
    box-shadow: 0 2px 4px rgba(0,0,0,.4);
  }
  .bpa { position: absolute; left: 0; right: 0; text-align: center; color: var(--white); font-family: var(--body); }
  .band { position: absolute; left: 0; right: 0; bottom: 0; background: var(--ink); color: var(--white); font-family: var(--body); font-weight: 700; text-align: center; }

  /* ---------- large front labels ---------- */
  .pack--large { top: 54px; width: 331px; height: 551px; }
  .pack--large .pattern-lime { right: 0; top: 0; width: 62px; height: 290px; border-bottom-left-radius: 60px 120px; }
  .pack--large .tag { left: 67px; top: 0; width: 203px; height: 28px; font-size: 19px; line-height: 28px; }
  .pack--large .label-box { left: 67px; top: 28px; width: 203px; height: 238px; }
  .pack--large .brand { top: 100px; font-size: 46px; }
  .pack--large .variant { top: 194px; font-size: 31px; }
  .pack--large .headline { top: 280px; font-size: 23px; }
  .pack--large .promise { top: 307px; font-size: 12px; }
  .pack--large .pattern-leaf { left: 0; right: 0; top: 336px; height: 175px; border-radius: 50% 50% 0 0 / 70% 70% 0 0; }
  .pack--large .badge { left: 126px; top: 391px; width: 80px; height: 80px; }
  .pack--large .bpa { top: 492px; font-size: 8px; }
  .pack--large .band { height: 40px; line-height: 40px; font-size: 10.5px; }

  /* ---------- small bottle labels ---------- */
  .pack--small { top: 110px; width: 175px; height: 445px; }
  .pack--small .pattern-lime { left: 0; right: 0; top: 0; height: 96px; border-bottom-left-radius: 50% 40px; border-bottom-right-radius: 50% 40px; }
  .pack--small .tag { left: 25px; top: 97px; width: 125px; height: 20px; font-size: 13px; line-height: 20px; }
  .pack--small .label-box { left: 25px; top: 117px; width: 125px; height: 145px; }
  .pack--small .brand { top: 55px; font-size: 28px; }
  .pack--small .variant { top: 117px; font-size: 19px; }
  .pack--small .headline { top: 271px; font-size: 15px; }
  .pack--small .promise { top: 310px; font-size: 8px; }
  .pack--small .pattern-leaf { left: 0; right: 0; top: 336px; height: 82px; border-radius: 50% 50% 0 0 / 60% 60% 0 0; }
  .pack--small .badge { left: 60px; top: 340px; width: 54px; height: 54px; }
  .pack--small .bpa { top: 402px; font-size: 5px; }
  .pack--small .band { height: 27px; line-height: 27px; font-size: 5.5px; }

  /* ---------- brand mark panel ---------- */
  .brand-panel { position: absolute; left: 102px; top: 672px; width: 353px; height: 427px; background: var(--ink); }
  .brand-panel__strap {
    height: 54px; line-height: 56px; text-align: center; color: var(--ink);
    font-family: var(--display); font-weight: 500; font-size: 33px; letter-spacing: .02em;
    background: linear-gradient(90deg, #8a6a35 0%, #d7b777 35%, #f1dcae 55%, #a9823f 100%);
  }
  .brand-panel__name { position: absolute; left: 0; right: 0; top: 240px; text-align: center; color: var(--white); font-family: var(--display); font-weight: 600; font-size: 88px; line-height: 1; letter-spacing: .02em; }

  /* ---------- carton dieline ---------- */
  .carton { position: absolute; left: 555px; top: 628px; width: 560px; height: 552px; }
  .carton svg { position: absolute; left: 0; top: 0; }
  .carton .abs { position: absolute; }
  .carton .tag { font-size: 11.5px; line-height: 18px; height: 18px; }
  .carton .label-box .brand { font-size: 27px; }
  .carton .label-box .variant { font-size: 20px; }
  .carton-front { --accent: var(--energy); }
  .carton-back { --accent: var(--energy); }
  .carton-back__mark { color: var(--white); font-family: var(--display); font-weight: 600; font-size: 12px; text-align: center; letter-spacing: .04em; }
  .carton-back__copy { color: var(--white); font-size: 6.4px; line-height: 1.3; text-align: justify; }
  .carton-back__copy p + p { margin-top: 6px; }
  .carton-back__nutrition { color: var(--white); font-size: 5.6px; line-height: 1.28; text-align: justify; }
  .carton-back__nutrition strong { display: block; font-size: 5.6px; }
  .carton-back__url { color: var(--lime); font-weight: 700; font-size: 7px; text-align: center; }
  .carton-tuck__text { color: var(--white); font-size: 6.6px; line-height: 1.25; text-align: center; transform: rotate(180deg); }
  .carton-side__text { color: var(--white); font-size: 5px; line-height: 1.35; transform-origin: 0 0; transform: rotate(90deg); white-space: nowrap; }
  .carton-spine { transform-origin: 0 0; transform: rotate(-90deg); text-align: center; white-space: nowrap; }
  .carton-spine__head { color: var(--lime); font-family: var(--display); font-weight: 600; font-size: 13px; line-height: 1.05; }
  .carton-spine__sub { color: var(--white); font-family: var(--display); font-weight: 500; font-size: 7.5px; line-height: 1.2; }
</style>
</head>
<body>

  <!-- Large label: Energy -->
  <section class="pack pack--large pack--energy" style="left:48px">
    <div class="pattern-lime" role="img" aria-label="Lime leaf line pattern"></div>
    <div class="tag">THRIVING DAYS GENTLY</div>
    <div class="label-box">
      <div class="brand">VERDANT</div>
      <div class="variant">ENERGY</div>
    </div>
    <div class="headline">EXTRACTING NATURE’S GOODNESS!</div>
    <div class="promise">Love the difference in 30 days or get 100% of your money back.</div>
    <div class="pattern-leaf" role="img" aria-label="Teal leaf line pattern"></div>
    <div class="badge" role="img" aria-label="Guarantee seal"></div>
    <div class="bpa">BPA FREE</div>
    <div class="band">NO ADDED COLOURING, NO ADDED SUGAR, NO GLUTEN</div>
  </section>

  <!-- Large label: Sleep -->
  <section class="pack pack--large pack--sleep" style="left:397px;width:328px">
    <div class="pattern-lime" role="img" aria-label="Lime leaf line pattern"></div>
    <div class="tag">THRIVING DAYS GENTLY</div>
    <div class="label-box">
      <div class="brand">VERDANT</div>
      <div class="variant">SLEEP</div>
    </div>
    <div class="headline">EXTRACTING NATURE’S GOODNESS!</div>
    <div class="promise">Love the difference in 30 days or get 100% of your money back.</div>
    <div class="pattern-leaf" role="img" aria-label="Teal leaf line pattern"></div>
    <div class="badge" role="img" aria-label="Guarantee seal"></div>
    <div class="bpa">BPA FREE</div>
    <div class="band">NO ADDED COLOURING, NO ADDED SUGAR, NO GLUTEN</div>
  </section>

  <!-- Small label: Sleep -->
  <section class="pack pack--small pack--sleep" style="left:773px">
    <div class="pattern-lime" role="img" aria-label="Lime leaf line pattern"></div>
    <div class="tag">THRIVING DAYS GENTLY</div>
    <div class="label-box">
      <div class="brand">VERDANT</div>
      <div class="variant">SLEEP</div>
    </div>
    <div class="headline">EXTRACTING NATURE’S<br>GOODNESS!</div>
    <div class="promise">Love the difference in 30 days or get<br>100% of your money back.</div>
    <div class="pattern-leaf" role="img" aria-label="Teal leaf line pattern"></div>
    <div class="badge" role="img" aria-label="Guarantee seal"></div>
    <div class="bpa">BPA FREE</div>
    <div class="band">NO ADDED COLOURING, NO ADDED SUGAR, NO GLUTEN</div>
  </section>

  <!-- Small label: Energy -->
  <section class="pack pack--small pack--energy" style="left:970px">
    <div class="pattern-lime" role="img" aria-label="Lime leaf line pattern"></div>
    <div class="tag">THRIVING DAYS GENTLY</div>
    <div class="label-box">
      <div class="brand">VERDANT</div>
      <div class="variant">ENERGY</div>
    </div>
    <div class="headline">EXTRACTING NATURE’S<br>GOODNESS!</div>
    <div class="promise">Love the difference in 30 days or get<br>100% of your money back.</div>
    <div class="pattern-leaf" role="img" aria-label="Teal leaf line pattern"></div>
    <div class="badge" role="img" aria-label="Guarantee seal"></div>
    <div class="bpa">BPA FREE</div>
    <div class="band">NO ADDED COLOURING, NO ADDED SUGAR, NO GLUTEN</div>
  </section>

  <!-- Brand mark panel -->
  <section class="brand-panel">
    <div class="brand-panel__strap">THRIVING DAYS GENTLY</div>
    <div class="brand-panel__name">VERDANT</div>
  </section>

  <!-- Carton dieline -->
  <section class="carton">
    <svg width="560" height="552" viewBox="0 0 560 552">
      <defs>
        <linearGradient id="limeFill" x1="0" y1="0" x2="1" y2="1">
          <stop offset="0" stop-color="#c9e02a"/>
          <stop offset="1" stop-color="#7fb83a"/>
        </linearGradient>
      </defs>
      <g fill="#0c6b66" stroke="#ffffff" stroke-width="0.8">
        <path d="M3 112 L37 102 L37 444 L3 434 Z"/>
        <path d="M37 102 L37 40 Q40 4 90 4 L195 4 Q242 4 245 40 L245 102 Z"/>
        <rect x="37" y="102" width="208" height="342"/>
        <rect x="245" y="102" width="65" height="342"/>
        <path d="M250 102 L254 60 Q278 48 305 60 L308 102 Z"/>
        <rect x="310" y="102" width="200" height="342"/>
        <rect x="510" y="102" width="45" height="342"/>
        <path d="M515 102 L520 60 L548 54 L555 102 Z"/>
        <path d="M37 444 L245 444 L238 480 L44 480 Z"/>
        <path d="M250 444 L306 444 L300 520 L256 520 Z"/>
        <path d="M310 444 L510 444 L510 520 Q505 547 470 547 L350 547 Q315 547 310 520 Z"/>
        <path d="M514 444 L552 444 L548 500 L518 500 Z"/>
      </g>
      <g role="img" aria-label="Lime leaf line pattern">
        <path d="M40 100 L40 42 Q44 8 90 8 L190 8 Q230 10 240 40 Q220 80 160 100 Z" fill="url(#limeFill)" opacity=".9"/>
        <path d="M258 60 Q278 50 302 60 L306 180 Q285 160 260 150 Z" fill="url(#limeFill)" opacity=".85"/>
        <path d="M440 102 L510 102 L510 150 Q470 140 440 102 Z" fill="url(#limeFill)"/>
        <path d="M520 60 L548 56 L555 102 L555 140 Q530 120 520 102 Z" fill="url(#limeFill)"/>
        <path d="M3 250 L37 230 L37 330 L3 340 Z" fill="url(#limeFill)" opacity=".8"/>
        <path d="M520 320 L555 290 L555 380 L520 400 Z" fill="url(#limeFill)" opacity=".8"/>
        <path d="M270 520 L300 470 L300 520 Z" fill="url(#limeFill)"/>
      </g>
      <g role="img" aria-label="Teal leaf line pattern">
        <path d="M37 420 Q141 280 245 420 Z" fill="#1f8a80" opacity=".7"/>
      </g>
      <rect x="37" y="420" width="208" height="24" fill="#262626"/>
    </svg>

    <!-- front panel -->
    <div class="carton-front">
      <div class="abs tag" style="left:81px;top:102px;width:126px">THRIVING DAYS GENTLY</div>
      <div class="abs label-box" style="left:81px;top:120px;width:126px;height:147px">
        <div class="brand" style="top:56px">VERDANT</div>
        <div class="variant" style="top:120px">ENERGY</div>
      </div>
      <div class="headline" style="left:37px;width:208px;top:277px;font-size:14px">EXTRACTING NATURE’S GOODNESS!</div>
      <div class="promise" style="left:37px;width:208px;top:294px;font-size:6.8px">Love the difference in 30 days or get 100% of your money back.</div>
      <div class="badge" role="img" aria-label="Guarantee seal" style="left:116px;top:342px;width:54px;height:54px"></div>
      <div class="bpa" style="left:37px;width:208px;top:408px;font-size:5px">BPA FREE</div>
      <div class="abs" style="left:37px;top:420px;width:208px;height:24px;line-height:24px;color:#fff;font-size:6px;font-weight:700;text-align:center">NO ADDED COLOURING, NO ADDED SUGAR, NO GLUTEN</div>
    </div>

    <!-- left side panel -->
    <div class="abs carton-side__text" style="left:297px;top:170px">
      Keep out of reach of children. Do not exceed the stated dose.<br>
      Consult your doctor if pregnant or taking medication.<br>
      Store in a cool dry place away from sunlight.<br>
      Food supplements are not a substitute for a varied diet.
    </div>
    <div class="badge" role="img" aria-label="Guarantee seal" style="left:262px;top:389px;width:34px;height:34px"></div>

    <!-- back panel -->
    <div class="carton-back">
      <div class="abs tag" style="left:350px;top:102px;width:124px">THRIVING DAYS GENTLY</div>
      <div class="abs carton-back__mark" style="left:310px;top:140px;width:200px">VERDANT</div>
      <div class="abs carton-back__copy" style="left:326px;top:170px;width:174px">
        <p>Verdant supplements are created in Britain by leading nutritionists. Mark Holloway, author of Verdant Way, ensures that each and every supplement is crafted in the most natural and Verdant way possible.</p>
        <p>Verdant’s purpose is to support health, wellbeing and longevity, so that we can all thrive in the modern world; an environment so alien to that in which we evolved. Embracing technology, research and science, we harness nature’s goodness - enabling us all to love life – naturally.</p>
      </div>
      <div class="abs carton-back__nutrition" style="left:326px;top:323px;width:174px">
        <strong>NUTRITIONAL INFORMATION PER 1 CAPSULE</strong>
        Vitamin C 80mg (100% NRV), Black Soy Bean 1000mg (Glycine max L.) (seeds) (from 50mg of 20:1 extract), Chitosan 50mg, Apple Cider Vinegar 17.5mg (Standardised to contain 35% Acetic Acid), White Kidney Bean Extract 1000mg (Phaseolus vulgaris L.) (bean) (from 50mg of 20:1 extract), Chromium 40mcg (100% NRV). Vitamin C 80mg (100% NRV), Black Soy Bean 1000mg (from 50mg of 20:1 extract), Chitosan 50mg, Apple Cider Vinegar 17.5mg, White Kidney Bean Extract 1000mg, Chromium 40mcg (100% NRV).
      </div>
      <div class="abs carton-back__url" style="left:310px;top:431px;width:200px">WWW.VERDANTSUPPLEMENTS.COM</div>
      <div class="abs carton-tuck__text" style="left:330px;top:460px;width:160px">TWICE KIND PROMISE. FOR EACH AND EVERY VERDANT SUPPLEMENT YOU TAKE, WE PROVIDE A SUPPLEMENT TO AN UNDER NOURISHED CHILD.</div>
    </div>

    <!-- right side panel -->
    <div class="abs carton-spine" style="left:516px;top:300px;width:190px">
      <div class="carton-spine__head">EXTRACTING NATURE’S GOODNESS!</div>
      <div class="carton-spine__sub">Love the difference in 30 days or get 100% of your money back.</div>
    </div>
  </section>

</body>
</html>
```